New Packaging and label for New Beard Oil and Shampoo brand from London

Oils, Shampoo ect .. Beard Oil Ingredients: Application Directions: Apply to beard by weight in a small amount of oil will naturally absorb. Leaving it soft & conditioned. Ingredients: Coconut oil, scented oil, Oud oil, vitamin E 100% Natural `i will have 5 types of oils Vanilla Oud Rose Oud Cocktail Tea tree Arabian Night

Target Market(s)

A fashionable well groomed professional gentleman who is willing to invest in his appearance.

Industry/Entity Type

It Company

Font styles to use
Sans Serif

Colors

Designer to choose colors to be used in the design.

Requirements
Must have
• Beard Oil Ingredients: Application Directions: Apply to a beard by a small amount of oil will naturally absorb. Leaving it soft & conditioned. Ingredients: Coconut Oil, Scented Oil, Oil Oud, Vitamin E 100% Natural 1.0z 30ml Made in Uk i will have 5 types of oils Vanilla Oud Rose Oud Cocktail Tea Tree Arabian Beard Night Shampoo APPLICATION DIRECTIONS Massage into the beard / hair and rinse out with warm water. Distorted shampoos, there are no nasty chemicals which are damaging your beard instead of the wheat proteins and oils that you add to the hair follicles with nutrients and naturally adding a protective coating. INGREDIENTS Aqua (Water), Capryl / caprylyl glucoside, Cocomidopropyl betaine, Glycerin (Veg), Xanthan gum, Phenoxyethanol, Hydrolysed wheat protein, Aloe barbadensis (Aloe vera) leaf powder, Sodium benzoate, Potassium sorbate1 3.4 oz, 100ml Cylinder packaging for the Oils, Box for the shampoo
Nice to have
• I want "London" written underneath the logo and oil name.

```html
<!DOCTYPE html>
<html lang="en">
<head>
<meta charset="utf-8">
<title>Noble Whisker – Vanilla Oud Beard Oil Labels</title>
<link href="https://fonts.googleapis.com/css2?family=Montserrat:wght@600&family=Quicksand:wght@400;500&display=swap" rel="stylesheet">
<style>
  :root {
    --page-bg: #ffffff;
    --brand-ink: #2b2b2b;
    --label-glow: #f4473c;
    --label-mid: #b5170f;
    --label-deep: #3a0604;
    --label-edge: #160202;
    --label-text: #ffffff;
    --rule: #f2f2f2;
  }
  * { box-sizing: border-box; margin: 0; padding: 0; }
  html, body {
    width: 1200px; height: 1200px; overflow: hidden;
    background: var(--page-bg);
  }
  .canvas {
    position: relative; width: 1200px; height: 1200px;
    font-family: "Quicksand", sans-serif;
  }
  .brand-mark {
    position: absolute; top: 138px; left: 0; width: 100%;
    text-align: center;
    font-family: "Montserrat", sans-serif; font-weight: 600;
    font-size: 44px; letter-spacing: 1px; color: var(--brand-ink);
  }
  .label-row {
    position: absolute; top: 640px; left: 0; width: 100%;
    display: flex; justify-content: center; gap: 10px;
  }
  .label {
    position: relative; width: 218px; height: 412px;
    border-radius: 10px;
    background: radial-gradient(ellipse 60% 55% at 50% 45%, var(--label-glow) 0%, var(--label-mid) 45%, var(--label-deep) 80%, var(--label-edge) 100%);
    color: var(--label-text); text-align: center;
    overflow: hidden;
  }
  .label__rule {
    position: absolute; left: 0; right: 0; top: 311px;
    height: 3px; background: var(--rule);
  }
  .label__block {
    position: absolute; left: 0; right: 0;
    font-size: 13px; line-height: 15.6px; font-weight: 400;
    white-space: nowrap;
  }
  .label--back .info--ingredients { top: 115px; }
  .label--back .info--directions { top: 197px; }
  .label--front .name { top: 101px; font-size: 22px; line-height: 26px; font-weight: 500; letter-spacing: 0.3px; }
  .label--front .city { top: 153px; font-size: 15px; line-height: 18px; letter-spacing: 5px; }
  .label--front .product { top: 238px; font-size: 24px; line-height: 30px; }
  .label--front .volume { top: 333px; font-size: 15px; line-height: 18px; }
  .label--maker .mfg { top: 89px; }
  .label--maker .name { top: 121px; font-size: 15px; line-height: 18px; font-weight: 500; }
  .label--maker .address { top: 163px; line-height: 16px; }
  .label--maker .icons {
    position: absolute; top: 212px; left: 0; right: 0;
    display: flex; justify-content: center; gap: 8px;
  }
  .label--maker .web { top: 256px; font-size: 15px; line-height: 18px; }
</style>
</head>
<body>
<main class="canvas">
  <div class="brand-mark">NOBLE WHISKER</div>

  <section class="label-row">
    <article class="label label--back">
      <p class="label__block info--ingredients">Ingredients:<br>Coconut oil, scented oil,<br>Oud oil, vitamin E<br>100% Natural</p>
      <p class="label__block info--directions">Directions:<br>Apply to beard by rubbing<br>in a small amount the oil<br>will naturally absorb.<br>Leaving it soft &amp;<br>conditioned.</p>
      <div class="label__rule"></div>
    </article>

    <article class="label label--front">
      <p class="label__block name">NOBLE WHISKER</p>
      <p class="label__block city">LONDON</p>
      <p class="label__block product">Vanilla Oud<br>Beard Oil</p>
      <div class="label__rule"></div>
      <p class="label__block volume">1 fl.oz | 30mL</p>
    </article>

    <article class="label label--maker">
      <p class="label__block mfg">MFG BY:</p>
      <p class="label__block name">NOBLE WHISKER</p>
      <p class="label__block address">City, State 00000 UK<br>(123) 456-7890</p>
      <div class="icons">
        <svg width="32" height="32" viewBox="0 0 32 32" role="img" aria-label="Cruelty-free badge"><circle cx="16" cy="16" r="15" fill="#ffffff"/><circle cx="16" cy="16" r="10" fill="#c41a10"/></svg>
        <svg width="32" height="32" viewBox="0 0 32 32" role="img" aria-label="Recycling symbol"><circle cx="16" cy="16" r="15" fill="#ffffff"/><path d="M9 18a7 7 0 0 1 12-7l2-2v7h-7l3-3a4 4 0 0 0-7 4z M23 14a7 7 0 0 1-12 7l-2 2v-7h7l-3 3a4 4 0 0 0 7-4z" fill="#c41a10"/></svg>
        <svg width="34" height="32" viewBox="0 0 34 32" role="img" aria-label="Period after opening"><ellipse cx="17" cy="11" rx="14" ry="6" fill="#ffffff"/><path d="M3 11v11c0 4 6 7 14 7s14-3 14-7V11c0 4-6 7-14 7S3 15 3 11z" fill="#ffffff"/></svg>
      </div>
      <p class="label__block web">yourcompany.com</p>
      <div class="label__rule"></div>
    </article>
  </section>
</main>
</body>
</html>
```